Education portal needs a new Email Creative Design

We could not decide on the creative earlier as we were unable to picture how will it look. Hence, we have added content so that we can choose the best design of all. Below is the content to be used for the email creative:
____________________________________
Did you know that 25% of all Americans have experienced at least one divorce?*
41% of first marriages end in divorce!!*

Over 1 million children are affected by divorce each year*

Become a Marriage and Family therapist - Achieve inner-happiness by helping individuals, families and couples resolve their struggles and enhance their lives.
Family Therapists are trained in various modes of therapy in order to prepare them for work with individuals, families, couples, and groups.

With proper training, you will be able to treat:
• Depression and other Affective Disorders
• Childhood Behavioral and Emotional Disorders
• Marital and Relationship Problems
• Conduct Disorder and Delinquency
• Substance Abuse
• Alcoholism
• Domestic Violence
• Severe Mental Illness
• Physical Illness

You could also qualify for financial aid* from the government to pursue this career..

Secure your life by earning upto $78,580* and attain peace of mind while helping others..

__________________________

These are the links to images we liked, but if you have something better, we would love to see them:
http://www.pictovale.example/photo/seperated-50317294?st=7kq2m81
http://www.pictovale.example/photo/domestic-violence-68204937?st=b4n9x52

We are an education portal offering options of schools, colleges, universities and courses to students and working professionals.

We are looking for an email creative which has great call-to-action; be creative and research more if you wish.
Incorporate call-to-action tabs, make it colorful, include pictures and content.
Also attached are industry standard creatives for your reference, let me know if you have any questions.
Updates

Please see new files uploaded

I have uploaded a new creative made by our design team. Follow similar guidelines

For those who have not submitted their designs, please send us soon. Thanks

We thought a content brief will do more justice to this design contest hence we have updated our brief with new content to create a newer design Please submit your designs soon. Thanks

Target Market(s)

25 to 50 years working professionals

Industry/Entity Type

Government

Font styles to use
Serif
Sans Serif
Decorative
Script

Requirements
Must have
• Call-to-action

```html
<!DOCTYPE html>
<html lang="en">
<head>
<meta charset="utf-8">
<title>Marriage and Family Therapist Career Flyer</title>
<link rel="stylesheet" href="https://fonts.googleapis.com/css2?family=Open+Sans:wght@400;600;700&display=swap">
<style>
  :root {
    --page-bg: #f3f3f3;
    --sheet: #ffffff;
    --wine: #6e1616;
    --wine-deep: #5a1010;
    --alert-red: #c8121c;
    --headline-red: #d8262e;
    --rose: rgba(186, 104, 96, 0.88);
    --body-text: #444444;
    --logo-gray: #555555;
    --white: #ffffff;
  }
  * { margin: 0; padding: 0; box-sizing: border-box; }
  html, body { width: 857px; height: 1200px; overflow: hidden; }
  body {
    background: var(--page-bg);
    font-family: "Open Sans", Arial, sans-serif;
    position: relative;
  }
  .flyer {
    position: absolute; left: 25px; top: 78px;
    width: 808px; height: 1045px;
    background: var(--sheet);
    box-shadow: 0 2px 8px rgba(0,0,0,0.25);
    overflow: hidden;
  }
  .hero {
    position: absolute; left: 0; top: 0; width: 808px; height: 558px;
    background: linear-gradient(120deg, #4a4446 0%, #8c8688 35%, #b9b6bb 60%, #d3d4dc 100%);
  }
  .hero-overlay { position: absolute; left: 0; top: 0; }
  .headline {
    position: absolute; left: 25px; top: 220px;
    color: var(--white); text-transform: uppercase; font-weight: 600; line-height: 1.2;
  }
  .headline .line-1 { font-size: 25px; }
  .headline .line-2 { font-size: 35px; color: var(--headline-red); font-weight: 700; line-height: 1.15; }
  .headline .line-3 { font-size: 30px; }
  .call-cta {
    position: absolute; left: 460px; top: 434px; width: 340px;
    text-align: center; color: var(--white);
  }
  .call-cta .label { font-size: 46px; font-weight: 600; line-height: 1.1; }
  .call-cta .number { font-size: 38px; font-weight: 400; line-height: 1.2; }
  .facts {
    position: absolute; left: 25px; top: 568px; width: 540px;
    color: var(--alert-red); font-size: 13.5px; font-weight: 600; line-height: 17px;
  }
  .intro {
    position: absolute; left: 22px; top: 604px; width: 470px;
    color: var(--body-text); font-size: 13px; line-height: 21px;
  }
  .train-banner { position: absolute; left: 0; top: 698px; }
  .train-banner span {
    position: absolute; left: 25px; top: 7px; white-space: nowrap;
    color: var(--white); font-size: 12.5px; font-weight: 600;
  }
  .treat-list {
    position: absolute; left: 22px; top: 738px; list-style: none;
    color: var(--body-text); font-size: 13px; line-height: 21.1px;
  }
  .treat-list li::before { content: "\2022\00a0"; }
  .earnings {
    position: absolute; left: 25px; top: 930px;
    color: var(--alert-red); font-size: 13.5px; font-weight: 700;
  }
  .side-photo { position: absolute; left: 415px; top: 582px; }
  .brand {
    position: absolute; left: 35px; top: 962px;
    color: var(--logo-gray); font-size: 48px; font-weight: 400; letter-spacing: 1px;
  }
  .contact { position: absolute; left: 497px; top: 972px; color: var(--body-text); font-size: 12.5px; }
  .contact .row { display: flex; gap: 22px; height: 22px; align-items: center; }
  .contact .item { display: flex; align-items: center; gap: 8px; }
  .contact svg { flex: none; }
</style>
</head>
<body>
  <main class="flyer">
    <section class="hero">
      <div class="hero-photo" role="img" aria-label="Close-up photo of a frightened child with a hand covering the mouth" style="position:absolute;inset:0;"></div>
      <svg class="hero-overlay" width="808" height="558" viewBox="0 0 808 558">
        <polygon points="0,18 420,18 523,278 420,518 0,518" fill="rgba(100,22,22,0.55)"/>
        <rect x="13" y="40" width="395" height="478" rx="12" fill="rgba(80,14,14,0.45)"/>
        <polygon points="468,414 808,414 808,558 410,558 440,500" fill="var(--rose)"/>
      </svg>
      <h1 class="headline">
        <div class="line-1">Over 1 million children</div>
        <div class="line-2">Are affected by</div>
        <div class="line-3">Divorce each year</div>
      </h1>
      <div class="call-cta">
        <div class="label">Call Now</div>
        <div class="number">1800 - 000 - 0000</div>
      </div>
    </section>

    <p class="facts">Did you know that 25% of all Americans have experienced at least one divorce?<br>41% of first marriages end in divorce!!</p>
    <p class="intro">Become a Marriage and Family therapist - Achieve inner-happiness by helping individuals, families and couples resolve their struggles and enhance their lives. Family Therapists are trained in various modes of therapy in order to prepare them for work with individuals, families, couples, and groups.</p>

    <div class="train-banner">
      <svg width="340" height="30" viewBox="0 0 340 30">
        <polygon points="0,0 322,0 336,15 322,30 0,30" fill="#e08070"/>
        <polygon points="0,0 316,0 330,15 316,30 0,30" fill="var(--wine)"/>
      </svg>
      <span>With proper training, you will be able to treat:</span>
    </div>

    <ul class="treat-list">
      <li>Depression and other Affective Disorders</li>
      <li>Childhood Behavioral and Emotional Disorders</li>
      <li>Marital and Relationship Problems</li>
      <li>Conduct Disorder and Delinquency</li>
      <li>Substance Abuse</li>
      <li>Alcoholism</li>
      <li>Domestic Violence</li>
      <li>Severe Mental Illness</li>
      <li>Physical Illness</li>
    </ul>

    <svg class="side-photo" width="393" height="340" viewBox="0 0 393 340">
      <defs>
        <linearGradient id="sidePhotoTone" x1="0" y1="0" x2="1" y2="1">
          <stop offset="0" stop-color="#1e3a48"/>
          <stop offset="0.5" stop-color="#34566a"/>
          <stop offset="1" stop-color="#1a2630"/>
        </linearGradient>
      </defs>
      <polygon points="0,168 110,16 200,16 200,325 110,325" fill="var(--wine-deep)"/>
      <polygon points="150,0 393,0 393,340 205,340 58,172" fill="url(#sidePhotoTone)" role="img" aria-label="Photo of a distressed young woman hiding her face in her arm"/>
    </svg>

    <p class="earnings">Secure your life by earning upto $78,580* and attain peace of mind while helping others..</p>

    <div class="brand">YOUR LOGO</div>

    <div class="contact">
      <div class="row">
        <div class="item">
          <svg width="14" height="12" viewBox="0 0 14 12"><polygon points="0,0 9,0 14,6 9,12 0,12" fill="var(--alert-red)"/></svg>
          <span>(201) 000 - 0000</span>
        </div>
        <div class="item">
          <svg width="14" height="12" viewBox="0 0 14 12"><polygon points="0,0 9,0 14,6 9,12 0,12" fill="var(--alert-red)"/></svg>
          <span>www.yoursite.example</span>
        </div>
      </div>
      <div class="row">
        <div class="item">
          <svg width="14" height="12" viewBox="0 0 14 12"><polygon points="0,0 9,0 14,6 9,12 0,12" fill="var(--alert-red)"/></svg>
          <span>100, Linden Grove Drive, Fairhaven, NY 10012</span>
        </div>
      </div>
    </div>
  </main>
</body>
</html>
```